Guaranteed Job - Sleek Sexy Business Card UV Spot

Im looking for a sleek and sexy business card, that resembles elite or VIP status status.
our business is corinvale.example
you can view our products on there, but our main audience for handing out our cards will be for people in the hospitality industry, so it will need to impress high management and CEO of hotels and restaurants, bars, clubs etc...
the card features will have UV spot on both sides, 400gsm stock. standard size.
Artwork should be 86 x 54mm + 2mm bleed = 90 x 58mm
it should have a nice "unique" uv spot pattern that highlights the card, not a repeated pattern, theres no originality there, and it will be disregarded.
The written material will be:
Corin Vale Hospitality College (logo)
Tobin Marsh
Director
Phone: 1300 615 737
Mobile: 0455 817 296
Email: info@corinvale.example
website: www.corinvale.example
I'm looking for originality here, i don't want just a simple stock card, want something that has a wow factor for people.
You will find the logo attached. you may invert the white to black words to suit the background as you please.
thank you and good luck
As a side note, ive received a lot of proposals, im too busy to give feedback to each and every one, so if i havent provided feedback for your design within 24 hours, then consider it not acceptable, and you could resubmit another design.
So far i have not seen any design that stood out for me, they all seem pretty generic. there nothing thats unique, i would figure for the amount that im offering, that people would put some more effort and creativity into the design.
so far over 200 designs submitted, and nothing i have seen looks very original, everything looks like a different variation of the same stuff, i said it very clearly i wanted something unique, the only thing that has come close to it so far is this one
Reason: Ive received alot of design concepts and i have reviewed everyone, but i havent had time to give feedback to every single one, only the ones that have interested me, if i havent responded, its because i havent found it good enough.
so far only a few design have been on par with what ive been looking for, an attractive eye popping design.
heres a few of them,
http://files.pixelbazaar.example/design_img/51736/62418/62418_2840915_51736_image.jpg
http://files.pixelbazaar.example/design_img/51736/68254/68254_2841377_51736_image.jpg
theyre, both unique and original, and eye catching, the only thing theyre missing is the sexyness.
if you still think you have some creativity left in your minds, then throw it on here.
Reason: Sorry guys for the delay, I was in a serious accident and out of commission for the past few months, I'm just slowly recovering now, please bare with me as i try to attend to this project, it may take me awhile as I have other projects that are on standby, I'm not 100% at the moment, so im extending the deadline for 2 weeks right now. Thanks for your patience.
Hospitality

```html
<!DOCTYPE html>
<html lang="en">
<head>
<meta charset="utf-8">
<title>Corin Vale Hospitality College – Business Card</title>
<link rel="stylesheet" href="https://fonts.googleapis.com/css2?family=Arimo:wght@400;700&display=swap">
<style>
  :root {
    --stage: #4d4d4d;
    --card: #000000;
    --card-sheen: #1c1c1c;
    --frame: #5aaee3;
    --ink: #ffffff;
    --muted: #9a9a9a;
    --accent: #5aaee3;
  }
  * { margin: 0; padding: 0; box-sizing: border-box; }
  html, body { width: 1200px; height: 900px; overflow: hidden; }
  body {
    background: var(--stage);
    font-family: "Arimo", Arial, sans-serif;
    color: var(--ink);
    position: relative;
  }
  .card {
    position: absolute;
    top: 300px;
    width: 525px;
    height: 330px;
    background: var(--card);
  }
  .card--front { left: 58px; width: 497px; }
  .card--back { left: 617px; }
  .card__texture {
    position: absolute;
    left: 30px; right: 30px; top: 28px; height: 200px;
    background: radial-gradient(ellipse at 50% 20%, var(--card-sheen) 0%, var(--card) 75%);
  }
  .card__frame {
    position: absolute;
    inset: 16px 17px 16px 16px;
    border: 6px solid var(--frame);
    border-radius: 26px;
  }
  .brand {
    position: absolute;
    font-weight: 700;
    color: var(--ink);
    text-transform: uppercase;
    line-height: 1.05;
  }
  .brand__mark {
    display: inline-block;
    background: var(--accent);
    vertical-align: top;
  }
  .card--front .brand { left: 120px; top: 96px; font-size: 30px; letter-spacing: 1px; }
  .card--front .brand__mark { width: 64px; height: 64px; margin-right: 18px; }
  .card--back .brand { left: 68px; top: 62px; font-size: 17px; letter-spacing: 0.5px; }
  .card--back .brand__mark { width: 34px; height: 34px; margin-right: 10px; }
  .brand__name { display: inline-block; }
  .brand__sub { display: block; font-size: 0.45em; letter-spacing: 1.5px; }
  .website {
    position: absolute;
    left: 0; right: 0; top: 240px;
    text-align: center;
    font-size: 14px;
  }
  .website strong { font-weight: 700; }
  .rule {
    position: absolute;
    height: 0;
    border-top: 2px dotted var(--accent);
    opacity: 0.85;
  }
  .card--front .rule { left: 164px; width: 196px; top: 263px; }
  .person {
    position: absolute;
    left: 77px; top: 162px;
    font-size: 16px;
  }
  .person__name {
    color: var(--accent);
    font-weight: 700;
    font-size: 20px;
    text-transform: uppercase;
  }
  .contact {
    position: absolute;
    left: 77px; top: 202px;
    font-size: 13px;
    font-weight: 700;
    line-height: 19px;
    list-style: none;
  }
  .contact__label { font-weight: 400; font-size: 11px; margin-right: 3px; }
  .card--back .rule--top { left: 77px; width: 210px; top: 191px; }
  .card--back .rule--bottom { left: 77px; width: 210px; top: 266px; }
</style>
</head>
<body>
  <section class="card card--front">
    <div class="card__texture" role="img" aria-label="Glossy tufted leather UV spot pattern"></div>
    <div class="card__frame"></div>
    <div class="brand">
      <span class="brand__mark"></span><span class="brand__name">Corin Vale<span class="brand__sub">Hospitality College</span></span>
    </div>
    <p class="website">www.<strong>corinvale</strong>.example</p>
    <div class="rule"></div>
  </section>

  <section class="card card--back">
    <div class="card__texture" role="img" aria-label="Glossy tufted leather UV spot pattern"></div>
    <div class="card__frame"></div>
    <div class="brand">
      <span class="brand__mark"></span><span class="brand__name">Corin Vale<span class="brand__sub">Hospitality College</span></span>
    </div>
    <p class="person"><span class="person__name">Tobin Marsh</span> Director</p>
    <div class="rule rule--top"></div>
    <ul class="contact">
      <li><span class="contact__label">p:</span>1300.615.737 <span class="contact__label">m:</span>0455.817.296</li>
      <li><span class="contact__label">e:</span>info@corinvale.example</li>
      <li><span class="contact__label">w:</span>www.corinvale.example</li>
    </ul>
    <div class="rule rule--bottom"></div>
  </section>
</body>
</html>
```